Meridian Harvest Partners- Web & Business card design for a new business within the Ag Sector

HELLO!!!!

We need your help in relation to web design (business cards and stationary if possible!) for a new company based in NSW, Australia.

The name of the business is: Meridian Harvest Partners (MHP). I have quickly mocked a webpage just to give you an idea of what we are looking for.... http://corvelland7.sitebuilderdemo.net/http

MHP is a strategic advisory, investment manager and problem solver within the Australian Agricultural sector.

Our Mission:

We are here to provide solutions to ALL of our Clients needs and desires within the Agricultural space.

Our Team:

Our team has worked with some of the largest & oldest Agricultural companies in Australia

We provide our Clients with a unique blend of the best Corporate as well as Operational experience that the Industry has to offer.

Client-driven Services Approach:

MHP offers a tailored service in order to meet the objectives and outcomes for each and every client.

Some of our services include:

- Food Security / Supply

- Procurement strategies within and across agricultural supply-chains

- Strategic Agribusiness advice for both Australian and Chinese based agricultural enterprises

- M&A / Due Diligence

- Corporate governance & risk management strategies.

I have attached a copy of our capability statement for background reading.

We look forward to receiving your designs!!!!!!!
Updates

Target Market(s)

Corporate, Family Offices, Food Services & Supermarkets - that are looking to obtain products within the agricultural space. Whether it be boxed beef, grain, live animals, advice - ie M&A, Due diligence - just think anything "Agricultural" and we can provide a solution

Industry/Entity Type

Agriculture

Contact Information for Business Card

See below

With respect to the business cards:

There are 2 Managing Directors:

1. Marcus Tilden
Managing Director
E: marcus.tilden@meridianharvestpartners.example
M: +61 400 913 642
W: www.meridianharvestpartners.example

2. Rachel Dunmore
Managing Director
E: rachel.dunmore@meridianharvestpartners.example
M: +61 400 276 418

Please see attached 2 * Files named Brenwick that outline a layout of business card that I like

Coding

Coded - Design and coding required

Number of Pages Required

5+ page

Font styles to use
Sans Serif
Other font styles liked:
• Calibri

Requirements
Must have
• I like the look of this website: http://fieldvoxtrend.example/
• And I like the themes in the website that I have mocked up: http://corvelland7.sitebuilderdemo.net/http
• The wow factor, with a professional twist.
• With respect to the website - would like it to follow the flow of the capability statement - ie with a home page, and the four additional pages:
• ABOUT US
• OUR SERVICES
• OUR TEAM
• CONTACT DETAILS
• The powerpoint presentation that I have attached is simply there for content direction - not design direction.
• As a result, am looking for web design / business card that stands out - is corporate - yet still agricultural feel.
• "capability statement" simply refers to a document that outlines our capabilities - and does not form part of the business name.
• A black angus cow, or a stalk of wheat - greens and yellows may better represent the Ag space.
• This s a draft mock-up of a web-site I created with one of those free web-page makers... This should give you a feel - crisp - whites - yet agricultural tones to highlight
• The attachments below should be used as inspiration - and don't need to be the actual shots used.

```html
<!DOCTYPE html>
<html lang="en">
<head>
<meta charset="utf-8">
<title>Meridian Harvest Partners</title>
<link rel="stylesheet" href="https://fonts.googleapis.com/css2?family=Open+Sans:wght@300;400;600&family=Tinos:wght@400;700&display=swap">
<style>
  :root {
    --green: #4f7a45;
    --green-dark: #3d5a36;
    --nav-bg: rgba(74, 104, 70, 0.9);
    --cream: #fdfdec;
    --ink: #2b2b2b;
    --footer: #3a3a3a;
    --white: #ffffff;
    --button: #4a5f45;
  }
  * { margin: 0; padding: 0; box-sizing: border-box; }
  html, body { width: 1200px; height: 2168px; overflow: hidden; background: var(--cream); }
  body { position: relative; font-family: "Tinos", "Times New Roman", serif; color: var(--ink); }

  .hero {
    position: absolute; left: 0; top: 0; width: 1200px; height: 820px;
    background: linear-gradient(180deg, #e9eef0 0%, #cdd9c9 28%, #8ea36c 48%, #5f7f3a 70%, #3f5f28 100%);
  }
  .brand {
    position: absolute; left: 40px; top: 0; width: 232px; height: 224px;
    background: rgba(253, 253, 236, 0.95);
    display: flex; flex-direction: column; align-items: center; justify-content: center; gap: 18px;
  }
  .brand-mark { width: 56px; height: 56px; border-radius: 50%; background: var(--green); }
  .brand-name {
    font-family: "Tinos", serif; font-size: 26px; line-height: 1.15; color: var(--green);
    text-align: center; padding: 0 14px;
  }
  .main-nav {
    position: absolute; left: 272px; top: 80px; width: 920px; height: 60px;
    background: var(--nav-bg); display: flex; align-items: center;
    font-family: "Open Sans", sans-serif; font-size: 22px; color: var(--white);
  }
  .main-nav a { color: var(--white); text-decoration: none; margin-left: 46px; }
  .main-nav .social {
    margin-left: auto; height: 60px; width: 150px; background: #3a3f38;
    display: flex; align-items: center; justify-content: center; gap: 8px;
  }
  .social span { width: 22px; height: 22px; border-radius: 50%; background: var(--white); }

  .hero-tag {
    position: absolute; left: 480px; top: 340px; width: 240px; height: 58px;
    background: #333; color: var(--white); font-family: "Open Sans", sans-serif;
    font-size: 28px; display: flex; align-items: center; justify-content: center; letter-spacing: 1px;
  }
  .hero-title {
    position: absolute; left: 0; width: 1200px; top: 412px; text-align: center;
    font-family: "Open Sans", sans-serif; font-weight: 400; font-size: 80px; letter-spacing: 4px; color: var(--white);
  }
  .hero-sub {
    position: absolute; left: 0; width: 1200px; top: 510px; text-align: center;
    font-family: "Open Sans", sans-serif; font-size: 40px; line-height: 52px; color: var(--white);
  }
  .button {
    position: absolute; background: var(--button); color: var(--white);
    font-family: "Open Sans", sans-serif; font-size: 20px; letter-spacing: 1px;
    display: flex; align-items: center; justify-content: center;
  }
  .hero .button { left: 492px; top: 628px; width: 212px; height: 50px; background: #3c3c3c; }
  .hero-arrow { position: absolute; top: 480px; }

  .intro { position: absolute; left: 0; top: 820px; width: 1200px; height: 472px; background: var(--cream); }
  .section-title { font-size: 36px; color: var(--green); font-weight: 400; letter-spacing: 1px; }
  .intro .text { position: absolute; left: 32px; top: 148px; width: 560px; }
  .intro p { font-size: 22px; line-height: 27px; margin-top: 18px; }
  .photo { position: absolute; }
  .harvest-photo { left: 628px; top: 68px; width: 540px; height: 324px;
    background: linear-gradient(180deg, #cfe0ee 0%, #a8c27a 45%, #c9a25a 70%, #a98445 100%); }

  .statement {
    position: absolute; left: 0; top: 1292px; width: 1200px; height: 320px;
    background: linear-gradient(180deg, #d9c6a3 0%, #cdb48a 50%, #bfa274 100%);
  }
  .statement p {
    position: absolute; left: 220px; width: 760px; top: 88px; text-align: center;
    font-size: 34px; line-height: 40px; color: #2a2a2a;
  }
  .statement .button { left: 496px; top: 220px; width: 208px; height: 46px; }

  .team { position: absolute; left: 0; top: 1612px; width: 1200px; height: 508px; background: var(--cream); }
  .sheep-photo { left: 32px; top: 84px; width: 540px; height: 324px;
    background: linear-gradient(180deg, #9fd05a 0%, #7cc03a 60%, #6aae2e 100%); }
  .team .text { position: absolute; left: 612px; top: 176px; width: 560px; }
  .team p { font-size: 22px; line-height: 28px; margin-top: 10px; }

  .site-footer {
    position: absolute; left: 0; top: 2120px; width: 1200px; height: 48px; background: var(--footer);
    color: #ddd; font-family: "Open Sans", sans-serif; font-size: 14px;
    display: flex; align-items: center; justify-content: center;
  }
</style>
</head>
<body>
  <header class="hero" role="img" aria-label="Aerial photograph of green rolling farmland hills under a pale sky">
    <div class="brand">
      <span class="brand-mark"></span>
      <span class="brand-name">Meridian Harvest Partners</span>
    </div>
    <nav class="main-nav">
      <a>Home</a><a>About Us</a><a>Services ▾</a><a>Our Team</a><a>Contact Details</a>
      <div class="social"><span></span><span></span><span></span><span></span></div>
    </nav>
    <div class="hero-tag">SERVICES</div>
    <h1 class="hero-title">TRULY UNIQUE</h1>
    <p class="hero-sub">operational farm managemen excellence<br>and investment</p>
    <div class="button">READ MORE</div>
    <svg class="hero-arrow" style="left:40px" width="40" height="80" viewBox="0 0 40 80"><polyline points="32,8 8,40 32,72" fill="none" stroke="#fff" stroke-width="8"/></svg>
    <svg class="hero-arrow" style="left:1104px" width="40" height="80" viewBox="0 0 40 80"><polyline points="8,8 32,40 8,72" fill="none" stroke="#fff" stroke-width="8"/></svg>
  </header>

  <section class="intro">
    <div class="text">
      <h2 class="section-title">MERIDIAN HARVEST PARTNERS</h2>
      <p>We are a strategic advisory, investment manager and problem solver with the Australian Agricultural sector.</p>
      <p>We are here to provide solutions to ALL of our Clients needs and desires within the Agricultural space.</p>
    </div>
    <div class="photo harvest-photo" role="img" aria-label="Green combine harvester cutting a golden wheat field"></div>
  </section>

  <section class="statement" role="img" aria-label="Close-up of ripe wheat stalks in soft light">
    <p>MHP is a strategic advisory, investment manager and problem solver within the Australian Agricultural sector.</p>
    <div class="button">READ MORE</div>
  </section>

  <section class="team">
    <div class="photo sheep-photo" role="img" aria-label="Sheep standing on bright green grass"></div>
    <div class="text">
      <h2 class="section-title">MERIDIAN HARVEST PARTNERS</h2>
      <p>We provide our Clients with a unique blend of the best Corporate as well as Operational experience that the Industry has to offer.</p>
    </div>
  </section>

  <footer class="site-footer">© Copyright to 2015 MeridianHarvestPartners. All rights reserved.</footer>
</body>
</html>
```